Crestline Venture Partners Business Card Redesign Project

CRESTLINE VENTURE PARTNERS
Our company needs to have its business cards redesigned as the current design no longer reflects the business brand or attracts the type of clientele we are seeking.

MUST LOOK
★ Upmarket
★ Reflect Quality
★ Corporate feel
★ Professional
★ Innovative
★ Colourful

MUST PROMOTE
★ Market Leader
★ Knowledge
★ Expertise
★ Experience
★ Solutions
★ Advice

MUST FEEL
★ Classy
★ Elegant
★ Savvy
★ Edgy
★ Upbeat

WHAT WE DO
Crestline Venture Partners provides project management and project controls consultancy services to companies in many industry sectors, within Australia and overseas. My company has developed a business brand through forging strong business relationships within industry. We provide innovative tools, concepts and solutions to management teams to assist them in better plan and managing there project portfolios.

SECTORS OF INDUSTRY WE SERVICE
★Oil & Gas
★Minerals & Metals
★Petrochemical
★Manufacturing
★Building & Construction
★Telecommunications
★Rail
★Civil

BUSINESS CARD DETAILS REQUIRED ON FRONT
Marcus Delane
Business Owner
Tel: 0438519627
Email: marcusdelane@crestlineventurepartners.com
Website: www.crestlineventurepartners.com.au

BUSINESS CARD DETAILS REQUIRED ON BACK
Providing | Knowledge | Expertise | Experience

ATTACHMENTS

Target Market(s)

Oil & Gas I Mining & Resources I Industry in General
Upmarket Clientele
Corporate World

Industry/Entity Type

Industry

Requirements
Must have
• Must be creative and a unique design
The business card must have information on the front and back

```html
<!DOCTYPE html>
<html lang="en">
<head>
<meta charset="utf-8">
<title>Crestline Venture Partners – Business Card</title>
<link rel="stylesheet" href="https://fonts.googleapis.com/css2?family=Open+Sans:wght@400;600;700&display=swap">
<style>
  :root {
    --page-bg: #ecebea;
    --card-white: #ffffff;
    --ink: #1c1c1c;
    --ink-soft: #555555;
    --brand-red: #e0201f;
    --grey-light: #dcdcdc;
    --grey-mid: #9b9b9b;
    --black: #111111;
    --blush-deep: #b98a8e;
    --blush-light: #f7eeee;
  }
  * { margin: 0; padding: 0; box-sizing: border-box; }
  html, body {
    width: 744px; height: 1200px; overflow: hidden;
    background: var(--page-bg);
    font-family: "Open Sans", Arial, sans-serif;
  }
  .canvas {
    width: 744px; height: 1200px;
    display: flex; flex-direction: column; align-items: center; justify-content: center;
    gap: 110px;
  }
  .card {
    position: relative; width: 640px; height: 366px; overflow: hidden;
    box-shadow: 0 6px 18px rgba(0,0,0,.18);
  }
  .card-front { background: var(--card-white); }
  .front-swoosh { position: absolute; inset: 0; }
  .holder { position: absolute; left: 44px; top: 86px; }
  .holder-name { font-size: 30px; font-weight: 600; color: var(--ink); line-height: 1.1; }
  .holder-role { font-size: 14px; color: var(--ink-soft); margin-top: 4px; }
  .contact-list { position: absolute; left: 44px; top: 182px; list-style: none; }
  .contact-list li {
    display: flex; align-items: center; gap: 9px;
    font-size: 12px; color: var(--ink); margin-bottom: 9px;
  }
  .contact-list svg { width: 13px; height: 13px; flex: none; }
  .front-brand {
    position: absolute; right: 34px; top: 170px; width: 150px; text-align: center;
    font-size: 13px; font-weight: 700; color: var(--brand-red); line-height: 1.3;
  }
  .card-back {
    background: radial-gradient(ellipse at 50% 42%, var(--blush-light) 0%, #e7d0d1 45%, var(--blush-deep) 100%);
    display: flex; flex-direction: column; align-items: center; justify-content: center;
  }
  .back-logo { display: flex; align-items: center; gap: 10px; }
  .back-logo-square { width: 26px; height: 26px; background: var(--brand-red); }
  .back-logo-name { font-size: 20px; font-weight: 700; color: var(--ink); letter-spacing: .5px; }
  .back-tagline { margin-top: 12px; font-size: 11px; color: var(--ink-soft); letter-spacing: .4px; }
</style>
</head>
<body>
<main class="canvas">
  <section class="card card-front">
    <svg class="front-swoosh" viewBox="0 0 640 366" preserveAspectRatio="none" aria-hidden="true">
      <defs>
        <linearGradient id="black-fill" x1="0" y1="0" x2="1" y2="1">
          <stop offset="0" stop-color="#3a3a3a"/>
          <stop offset="1" stop-color="#050505"/>
        </linearGradient>
      </defs>
      <path d="M310 0 C430 60 440 250 230 366 L640 366 L640 0 Z" fill="var(--grey-light)"/>
      <path d="M365 0 C475 70 475 260 285 366 L640 366 L640 0 Z" fill="var(--grey-mid)"/>
      <path d="M405 0 C505 80 505 270 335 366 L640 366 L640 0 Z" fill="url(#black-fill)"/>
      <path d="M0 352 L640 352 L640 366 L0 366 Z" fill="var(--black)"/>
    </svg>
    <div class="holder">
      <h1 class="holder-name">Marcus Delane</h1>
      <p class="holder-role">Business Owner</p>
    </div>
    <ul class="contact-list">
      <li>
        <svg viewBox="0 0 16 16"><path d="M4 1h3l1 4-2 1a9 9 0 0 0 4 4l1-2 4 1v3a2 2 0 0 1-2 2A13 13 0 0 1 2 3a2 2 0 0 1 2-2z" fill="var(--ink)"/></svg>
        0438519627
      </li>
      <li>
        <svg viewBox="0 0 16 16"><rect x="1" y="3" width="14" height="10" fill="none" stroke="var(--ink)" stroke-width="1.5"/><path d="M1 3l7 6 7-6" fill="none" stroke="var(--ink)" stroke-width="1.5"/></svg>
        marcusdelane@crestlineventurepartners.com
      </li>
      <li>
        <svg viewBox="0 0 16 16"><circle cx="8" cy="8" r="6.5" fill="none" stroke="var(--ink)" stroke-width="1.4"/><ellipse cx="8" cy="8" rx="2.8" ry="6.5" fill="none" stroke="var(--ink)" stroke-width="1.2"/><path d="M1.5 8h13" stroke="var(--ink)" stroke-width="1.2"/></svg>
        www.crestlineventurepartners.com.au
      </li>
    </ul>
    <p class="front-brand">Crestline Venture Partners</p>
  </section>

  <section class="card card-back">
    <div class="back-logo">
      <span class="back-logo-square"></span>
      <span class="back-logo-name">CRESTLINE VENTURE PARTNERS</span>
    </div>
    <p class="back-tagline">Providing | Knowledge | Expertise | Experience</p>
  </section>
</main>
</body>
</html>
```